Customs House descriptive business cards

We require a two-sided business card that has a simple yet elegant design. We want to be able to promote our services as a customs house. This card should include our logo, contact info and services offered with the logo being on one side and the contact info and services on the flip side

Target Market(s)

Importers / exporters to and from the Bahamas

Industry/Entity Type

Logistics

Contact Information for Business Card

The front side of the card could have the logo and the flip side should have the other relevant info

Font styles to use
Serif

Colors

Designer to choose colors to be used in the design.

Requirements
Must have
• (Harbourline Agents Ltd) Logo, address and contact info also services:
• import customs clearance, Delivery & HAndling services,Florida pickups, Export packing & Crating Services, export customs clearance, Consulting

```html
<!DOCTYPE html>
<html lang="en">
<head>
<meta charset="utf-8">
<title>Harbourline Agents Ltd — Business Card</title>
<link href="https://fonts.googleapis.com/css2?family=EB+Garamond:wght@400;500&display=swap" rel="stylesheet">
<style>
  :root {
    --backdrop: #3a3a3c;
    --brand-blue: #1f63b5;
    --brand-blue-light: #2a8bd6;
    --brand-blue-deep: #1a5eb2;
    --paper: #ffffff;
    --rule-grey: #b9bcc1;
    --ink-grey: #5a5d62;
    --band-text: #dce8f7;
  }
  * { margin: 0; padding: 0; box-sizing: border-box; }
  html, body {
    width: 1200px; height: 900px; overflow: hidden;
    background: var(--backdrop);
    font-family: "EB Garamond", Georgia, serif;
  }
  .sheet {
    width: 1200px; height: 900px;
    display: flex; align-items: center; justify-content: center; gap: 48px;
  }
  .card {
    width: 520px; height: 298px; position: relative; overflow: hidden;
  }

  /* Logo side */
  .card--front {
    background: linear-gradient(135deg, var(--brand-blue-light) 0%, var(--brand-blue) 100%);
    display: flex; align-items: center; justify-content: center;
  }
  .wordmark {
    display: flex; align-items: center; gap: 12px;
    color: var(--paper); font-weight: 500; font-size: 34px; letter-spacing: 0.5px;
  }
  .wordmark__dot {
    width: 14px; height: 14px; border-radius: 50%; background: currentColor;
  }

  /* Contact side */
  .card--back { background: var(--paper); }
  .card__top {
    position: absolute; left: 0; top: 0; right: 0; height: 188px;
  }
  .card__top .wordmark {
    position: absolute; left: 26px; top: 24px;
    color: var(--brand-blue); font-size: 24px; gap: 9px;
  }
  .card__top .wordmark__dot { width: 10px; height: 10px; }
  .services {
    position: absolute; left: 26px; top: 72px; width: 292px;
    list-style: none;
    display: grid; grid-template-columns: 146px 146px; row-gap: 2px;
    font-size: 12px; line-height: 15px; color: var(--ink-grey);
  }
  .services li { display: flex; align-items: center; gap: 5px; white-space: nowrap; }
  .services li::before {
    content: ""; width: 4px; height: 4px; border-radius: 50%;
    background: var(--brand-blue); flex: none;
  }
  .holder {
    position: absolute; right: 30px; bottom: 16px; text-align: right;
  }
  .holder__name {
    color: var(--brand-blue); font-size: 22px; letter-spacing: 1.5px;
    text-transform: uppercase; font-weight: 500; line-height: 1.15;
  }
  .holder__role { color: var(--ink-grey); font-size: 14px; margin-top: 2px; }
  .divider {
    position: absolute; left: 0; right: 0; top: 188px; height: 5px;
    background: var(--rule-grey);
  }
  .band {
    position: absolute; left: 0; right: 0; top: 193px; bottom: 0;
    background: var(--brand-blue-deep);
    color: var(--band-text);
    display: flex; justify-content: space-between; align-items: flex-end;
    padding: 18px 28px 20px 26px;
  }
  .contact-list { list-style: none; font-size: 14px; line-height: 1.55; align-self: flex-start; }
  .contact-list li { display: flex; align-items: center; gap: 8px; }
  .contact-list svg { width: 10px; height: 10px; fill: var(--band-text); }
  .address { font-size: 17px; line-height: 1.3; text-align: right; color: var(--paper); }
</style>
</head>
<body>
<main class="sheet">
  <section class="card card--front" aria-label="Card front">
    <div class="wordmark"><span class="wordmark__dot"></span>Harbourline Agents Ltd</div>
  </section>

  <section class="card card--back" aria-label="Card back">
    <div class="card__top">
      <div class="wordmark"><span class="wordmark__dot"></span>Harbourline Agents Ltd</div>
      <ul class="services" aria-label="Services">
        <li>Import Customs Clearance</li>
        <li>Export Customs Clearance</li>
        <li>Delivery &amp; Handling</li>
        <li>Export Packing &amp; Crating</li>
        <li>Florida Pickups</li>
        <li>Consulting</li>
      </ul>
      <div class="holder">
        <p class="holder__name">Daniel Reyes</p>
        <p class="holder__role">Director</p>
      </div>
    </div>
    <div class="divider"></div>
    <div class="band">
      <ul class="contact-list">
        <li>
          <svg viewBox="0 0 10 10" aria-hidden="true"><path d="M2 0.5 L3.6 2.6 L2.8 3.6 Q4 5.8 6.4 7.2 L7.4 6.4 L9.5 8 L8.4 9.5 Q3.5 9 0.5 1.6 Z"/></svg>
          407.555.0142
        </li>
        <li>
          <svg viewBox="0 0 10 10" aria-hidden="true"><path d="M0.5 2 H9.5 V8 H0.5 Z M1.2 2.6 L5 5.4 L8.8 2.6" fill="none" stroke="#dce8f7" stroke-width="1"/></svg>
          info@harbourlineagents.com
        </li>
        <li>
          <svg viewBox="0 0 10 10" aria-hidden="true"><circle cx="5" cy="5" r="4.4" fill="none" stroke="#dce8f7" stroke-width="1"/><path d="M0.6 5 H9.4 M5 0.6 Q2.4 5 5 9.4 M5 0.6 Q7.6 5 5 9.4" fill="none" stroke="#dce8f7" stroke-width="0.8"/></svg>
          www.harbourlineagents.com
        </li>
      </ul>
      <p class="address">218 Bayview Ave Suite 12<br>Orlando, Florida, 32801</p>
    </div>
  </section>
</main>
</body>
</html>
```